Web Design Project

We need a web design for a new business in Orland Park, IL.
We are a restaurant meal delivery business. We deliver from a variety of restaurants. We gives our customers an alternative to just pizza delivery.

Websites we like:
http://www.quillbarkrunners.com/
https://www.fennowmealpost.com/Default.asp
www.brambletrayhaul.com/

Our current website is www.zestwickdrop.com(not to be used as a guide, i'm looking for an original design)
Updates

Please no pictures of anything associated with Pizza.  We are a restaurant delivery business that gives our customers an alternative to just pizza delivery. 

This is my original logo.  I uploaded the file to the job brief and updated the brief some.

Target Market(s)

Two income households with children.

Industry/Entity Type

Business

Requirements
Must have
• Order Now button,and sliding photographs of food.
Nice to have
• a background other than white(it can be white if it works with the design)
Should not have
• A picture of pizza that cant be changed. It is ok if the photo is apart of sliding photo's, but pizza cant be the main focus of our delivery service.

```html
<!DOCTYPE html>
<html lang="en">
<head>
<meta charset="utf-8">
<title>Zestwick Drop – Restaurant Delivery</title>
<link rel="stylesheet" href="https://fonts.googleapis.com/css2?family=Ubuntu:wght@400;500;700&family=Norican&family=Arimo:wght@400;700&display=swap">
<style>
:root{
  --gold:#e2b511;
  --gold-dark:#c99c08;
  --gold-soft:#e8c23a;
  --red:#b3060b;
  --red-deep:#7a0a0a;
  --maroon:#5b0b0b;
  --cream:#f5f0e0;
  --ink:#2a2a2a;
  --white:#ffffff;
}
*{margin:0;padding:0;box-sizing:border-box}
html,body{width:935px;height:1200px;overflow:hidden}
body{position:relative;background:var(--white);font-family:'Arimo',Arial,sans-serif;color:var(--ink)}
.abs{position:absolute}

/* Header */
.top-strip{left:0;top:0;width:935px;height:5px;background:var(--red-deep)}
.header{left:0;top:5px;width:935px;height:162px;background:var(--gold)}
.account-tab{left:684px;top:5px;width:157px;height:29px;display:flex;
  clip-path:polygon(6px 0,100% 0,100% 100%,0 100%)}
.account-tab a{flex:1;display:flex;align-items:center;justify-content:center;
  font:700 11px 'Ubuntu',sans-serif;color:var(--gold);text-decoration:none;letter-spacing:.3px}
.account-tab .login{background:var(--red-deep)}
.account-tab .register{background:var(--maroon)}
.brand{left:96px;top:92px;display:flex;align-items:center;gap:8px}
.brand-dot{width:18px;height:18px;border-radius:50%;background:var(--red)}
.brand-name{font:700 26px 'Ubuntu',sans-serif;color:var(--red)}
.order-now{left:648px;top:52px;width:182px;text-align:center;font:36px 'Norican',cursive;color:var(--red)}
.order-underline{left:650px;top:98px}
.phone{left:640px;top:114px;width:200px;text-align:right;font:400 28px 'Ubuntu',sans-serif;color:var(--red);letter-spacing:.5px}

/* Navigation */
.nav{left:0;top:167px;width:935px;height:41px;background:var(--red)}
.nav a{position:absolute;top:14px;font:700 11px 'Ubuntu',sans-serif;color:var(--white);text-decoration:none;letter-spacing:.2px}
.nav a.active{color:var(--gold-soft)}
.nav-scallop{left:0;top:206px}

/* Hero slider */
.hero{left:0;top:208px;width:935px;height:392px;
  background:radial-gradient(ellipse at 30% 45%,#c94a2a 0%,#9a3a22 30%,transparent 60%),
  radial-gradient(ellipse at 75% 55%,#d8703a 0%,transparent 55%),
  linear-gradient(135deg,#7c3a22 0%,#b2552d 40%,#8e3b1f 70%,#5a2614 100%)}
.slide-caption{left:92px;top:357px;width:523px;height:80px;background:rgba(255,255,255,.72)}
.slide-title{left:92px;top:367px;width:523px;text-align:center;font:700 19px 'Ubuntu',sans-serif;color:#222;letter-spacing:.2px}
.slide-btn{left:245px;top:398px;width:215px;height:28px;background:linear-gradient(#e7c33a,#cf9f0a);
  display:flex;align-items:center;justify-content:center;gap:8px;font:500 14px 'Ubuntu',sans-serif;color:var(--white)}
.slider-arrow{top:371px;width:37px;height:34px;background:rgba(255,255,255,.85);display:flex;align-items:center;justify-content:center}

/* Feature cards */
.card{top:502px;width:172px;height:225px;background:var(--white);box-shadow:0 14px 16px -10px rgba(0,0,0,.18);text-align:center}
.card-title{margin-top:10px;font:22px 'Norican',cursive;color:var(--red)}
.card-rule{margin:6px 0 0;border-top:1px dashed #e2c7c7}
.card-mark{width:12px;height:3px;margin:-2px auto 0;background:var(--red);border-radius:2px;opacity:.6}
.card-icon{height:50px;margin-top:12px;display:flex;align-items:center;justify-content:center}
.card-text{margin:14px 14px 0;font:9px/14px 'Arimo',Arial,sans-serif;color:#222}
.card-more{display:inline-flex;align-items:center;justify-content:center;margin-top:8px;width:70px;height:22px;background:var(--gold);font:700 11px 'Ubuntu',sans-serif;color:var(--red)}

/* Welcome */
.welcome{left:93px;top:763px;width:748px;height:177px;background:var(--gold)}
.welcome-frame{left:99px;top:769px;width:736px;height:165px;border:1px solid rgba(255,255,255,.45)}
.welcome-title{left:110px;top:796px;font:34px/1 'Norican',cursive;color:var(--red)}
.welcome-sub{left:110px;top:843px;font:22px/30px 'Norican',cursive;color:var(--red)}
.welcome-divider{left:273px;top:788px;width:1px;height:132px;background:rgba(120,80,0,.45)}
.welcome-lead{left:287px;top:791px;width:540px;font:700 14px/17px 'Arimo',Arial,sans-serif;color:#2b2b2b}
.welcome-body{left:287px;top:837px;width:540px;font:700 10.3px/13px 'Arimo',Arial,sans-serif;color:var(--white)}

/* Footer */
.footer{left:0;top:969px;width:935px;height:175px;background:var(--cream);border-top:1px solid #e3d9b8}
.footer-col{top:980px}
.footer-heading{font:500 11px 'Ubuntu',sans-serif;color:var(--gold-dark);letter-spacing:.3px;margin-bottom:14px}
.footer-links li{list-style:none;font:9px 'Arimo',Arial,sans-serif;color:#333;margin-bottom:11px}
.hours p{font:9px/14px 'Arimo',Arial,sans-serif;color:#333}
.hours p+p{margin-top:14px}
.field{width:171px;height:21px;border:1px solid #ddd;border-radius:3px;background:var(--white);
  font:9px 'Arimo',Arial,sans-serif;color:#888;padding:5px 6px;margin-bottom:6px;box-shadow:inset 0 1px 2px rgba(0,0,0,.06)}
.field.message{height:40px}
.submit{margin-left:101px;width:70px;height:20px;border-radius:3px;background:linear-gradient(#e7c33a,#c89a0a);
  font:700 10px 'Ubuntu',sans-serif;color:var(--white);display:flex;align-items:center;justify-content:center}
.social li{list-style:none;display:flex;align-items:center;gap:10px;margin-bottom:10px;font:9.5px 'Arimo',Arial,sans-serif;color:#333}
.social-dot{width:21px;height:21px;border-radius:50%;border:2px solid var(--white);box-shadow:0 0 0 1px #ddd}
.dot-a{background:#3b5b98}.dot-b{background:#2fa9e0}.dot-c{background:#c8201e}.dot-d{background:#e8621c}

.bottom-bar{left:0;top:1144px;width:935px;height:56px;background:var(--gold)}
.copyright{left:0;top:1163px;width:935px;text-align:center;font:9.5px 'Arimo',Arial,sans-serif;color:#3a2a00}
</style>
</head>
<body>

<div class="abs header"></div>
<div class="abs top-strip"></div>
<nav class="abs account-tab"><a class="login">LOGIN</a><a class="register">REGISTER</a></nav>

<div class="abs brand"><span class="brand-dot"></span><span class="brand-name">Zestwick Drop</span></div>

<div class="abs order-now">Order Now</div>
<svg class="abs order-underline" width="180" height="8" viewBox="0 0 180 8"><path d="M2 6 Q90 -1 178 5" fill="none" stroke="#b3060b" stroke-width="1.4"/></svg>
<div class="abs phone">(000)&nbsp;000 0000</div>

<nav class="abs nav">
  <a class="active" style="left:114px">HOME</a>
  <a style="left:186px">RESTAURANTS</a>
  <a style="left:296px">HOW DO I ORDER?</a>
  <a style="left:432px">CORPORATE</a>
  <a style="left:535px">GIFT CERTIFICATE</a>
  <a style="left:663px">ABOUT US</a>
  <a style="left:754px">CONTACT US</a>
</nav>

<div class="abs hero" role="img" aria-label="Slideshow photo of stir-fried prawns with peppers, onions and sesame seeds"></div>
<svg class="abs nav-scallop" width="935" height="6" viewBox="0 0 935 6">
  <defs><pattern id="scallop" width="13" height="6" patternUnits="userSpaceOnUse"><path d="M0 0 H13 Q6.5 9 0 0Z" fill="#e2b511"/></pattern></defs>
  <rect width="935" height="6" fill="url(#scallop)"/>
</svg>

<div class="abs slide-caption"></div>
<div class="abs slide-title">KING PRAWN PAKORA CHINESE OMELETTE RECIPE</div>
<div class="abs slide-btn">PLACE ORDER FOR DELIVER
  <svg width="9" height="13" viewBox="0 0 9 13"><path d="M1.5 1.5 L7 6.5 L1.5 11.5" fill="none" stroke="#8a0a0a" stroke-width="3"/></svg></div>
<div class="abs slider-arrow" style="left:0"><svg width="14" height="18" viewBox="0 0 14 18"><path d="M11 2 L4 9 L11 16" fill="none" stroke="#d9a90d" stroke-width="4"/></svg></div>
<div class="abs slider-arrow" style="left:898px"><svg width="14" height="18" viewBox="0 0 14 18"><path d="M3 2 L10 9 L3 16" fill="none" stroke="#d9a90d" stroke-width="4"/></svg></div>

<!-- Feature cards -->
<section class="abs card" style="left:94px">
  <div class="card-title">Our Gifts</div><div class="card-rule"></div><div class="card-mark"></div>
  <div class="card-icon"><svg width="32" height="36" viewBox="0 0 32 36" fill="#333"><rect x="2" y="10" width="28" height="8"/><rect x="4" y="20" width="24" height="15"/><rect x="14" y="10" width="4" height="25" fill="#fff"/><path d="M16 10 C8 0 2 6 9 10Z M16 10 C24 0 30 6 23 10Z"/></svg></div>
  <p class="card-text">Lorem ipsum dolor sit amet, con-seuer adipiscing elit. Praesent ves-tibulum molestie lacus. Aenean nonummy.</p>
  <span class="card-more">MORE »</span>
</section>
<section class="abs card" style="left:287px">
  <div class="card-title">Our Menus</div><div class="card-rule"></div><div class="card-mark"></div>
  <div class="card-icon"><svg width="38" height="38" viewBox="0 0 38 38" fill="#333"><path d="M4 8 L30 34 L34 30 L18 14 C22 8 16 2 10 2Z"/><path d="M34 6 L8 32 L4 34 L6 30 L24 12 L26 4 L28 6 L30 2 L32 6 L36 4Z"/></svg></div>
  <p class="card-text">Lorem ipsum dolor sit amet, con-seuer adipiscing elit. Praesent ves-tibulum molestie lacus. Aenean nonummy.</p>
  <span class="card-more">MORE »</span>
</section>
<section class="abs card" style="left:479px">
  <div class="card-title">Specials</div><div class="card-rule"></div><div class="card-mark"></div>
  <div class="card-icon"><svg width="42" height="34" viewBox="0 0 42 34" fill="#333"><path d="M4 10 C2 2 14 -2 21 2 C28 -2 40 2 38 10 L32 24 H10Z"/><rect x="10" y="26" width="22" height="6" rx="1"/><path d="M15 8 V22 M21 6 V22 M27 8 V22" stroke="#fff" stroke-width="2"/></svg></div>
  <p class="card-text">Lorem ipsum dolor sit amet, con-seuer adipiscing elit. Praesent ves-tibulum molestie lacus. Aenean nonummy.</p>
  <span class="card-more">MORE »</span>
</section>
<section class="abs card" style="left:671px">
  <div class="card-title">Dessert</div><div class="card-rule"></div><div class="card-mark"></div>
  <div class="card-icon"><svg width="34" height="38" viewBox="0 0 34 38" fill="#333"><circle cx="17" cy="4" r="3"/><path d="M4 18 C4 6 30 6 30 18 C33 18 33 22 30 22 H4 C1 22 1 18 4 18Z"/><path d="M5 24 H29 L26 37 H8Z"/></svg></div>
  <p class="card-text">Lorem ipsum dolor sit amet, con-seuer adipiscing elit. Praesent ves-tibulum molestie lacus. Aenean nonummy.</p>
  <span class="card-more">MORE »</span>
</section>

<!-- Welcome -->
<div class="abs welcome"></div>
<div class="abs welcome-frame"></div>
<div class="abs welcome-title">Welcome</div>
<div class="abs welcome-sub">to<br>Zestwick Drop</div>
<div class="abs welcome-divider"></div>
<h2 class="abs welcome-lead">Sed ut perspiciatis unde omnis iste natus error sit voluptatem accusantium doloremque laudantium, totam rem aperiam,</h2>
<p class="abs welcome-body">eaque ipsa quae ab illo inventore veritatis et quasi architecto beatae vitae dicta sunt explicabo. Nemo enim ipsam voluptatem quia voluptas sit aspernatur aut odit aut fugit, sed quia consequuntur magni do-lores eos qui ratione voluptatem sequi nesciunt. Neque porro quisquam est, qui dolorem ipsum quia dolor sit amet, consectetur, adipisci velit, sed quia non numquam eius modi tempora incidunt ut labore et dolore magnam aliquam quaerat voluptatem. Ut enim ad minima veniam, quis nostrum exercitationem ullam corporis suscipit laboriosam,</p>

<!-- Footer -->
<footer class="abs footer"></footer>
<div class="abs footer-col" style="left:102px">
  <h3 class="footer-heading">INFORMATION</h3>
  <ul class="footer-links"><li>Place Order</li><li>Menus</li><li>Catering Menus</li><li>Customer Center</li><li>Employment</li><li>More</li></ul>
</div>
<div class="abs footer-col hours" style="left:288px">
  <h3 class="footer-heading">HOURS OF OPERATION</h3>
  <p>Lunch<br>Monday To Friday<br>8:30 AM to 1:00 PM (sometimes later)</p>
  <p>Dinner<br>Sunday to Thursday 4:00 PM to 8:30 PM<br>Friday and Saturday<br>4:00 PM to 9:00 PM</p>
</div>
<div class="abs footer-col" style="left:475px">
  <h3 class="footer-heading">CONTACT INFO</h3>
  <div class="field">Name</div>
  <div class="field">Email</div>
  <div class="field message">Message</div>
  <div class="submit">SUBMIT</div>
</div>
<div class="abs footer-col" style="left:661px">
  <h3 class="footer-heading">GET IN TOUCH</h3>
  <ul class="social">
    <li><span class="social-dot dot-a"></span>FRIENDLOOP</li>
    <li><span class="social-dot dot-b"></span>CHIRPLINE</li>
    <li><span class="social-dot dot-c"></span>REELCAST</li>
    <li><span class="social-dot dot-d"></span>RSS FEED</li>
  </ul>
</div>

<div class="abs bottom-bar"></div>
<div class="abs copyright">© 2012 ZESTWICKDROP &nbsp;|&nbsp; PRIVACY POLICY</div>

</body>
</html>
```